Reiki business card

Please see uploaded files. There is a word document on there explaining what is required and what the other uploaded files are for. I am after a soft, relaxing, warm welcoming feel to the card. Thank you.

Business

```html
<!DOCTYPE html>
<html lang="en">
<head>
<meta charset="utf-8">
<title>Reiki for Families &amp; Pets – Business Card</title>
<link rel="stylesheet" href="https://fonts.googleapis.com/css2?family=Tinos:ital@1&display=swap">
<style>
  :root {
    --page: #ffffff;
    --frame-light: #2bc0f5;
    --frame-soft: #4aa8ec;
    --sky-deep: #0b62b8;
    --sky-mid: #2a9ee6;
    --sky-glow: #5cc3f2;
    --back-deep: #1570c2;
    --back-glow: #52b4ea;
    --ink: #ffffff;
    --illustration: #f4fbff;
  }
  html, body {
    margin: 0;
    padding: 0;
    width: 1200px;
    height: 1161px;
    overflow: hidden;
    background: var(--page);
  }
  .canvas {
    position: relative;
    width: 1200px;
    height: 1161px;
    font-family: "Tinos", "Times New Roman", serif;
    font-style: italic;
    color: var(--ink);
  }
  .card {
    position: absolute;
    left: 92px;
    width: 1044px;
    box-sizing: border-box;
    border: 7px solid var(--frame-light);
    overflow: hidden;
  }
  .card--front {
    top: 14px;
    height: 522px;
    background:
      radial-gradient(ellipse 45% 55% at 72% 52%, var(--sky-glow) 0%, rgba(92,195,242,0) 100%),
      radial-gradient(ellipse 75% 80% at 50% 45%, var(--sky-mid) 0%, var(--sky-deep) 100%);
  }
  .card--back {
    top: 618px;
    height: 524px;
    border-color: var(--frame-soft);
    background:
      radial-gradient(ellipse 60% 55% at 55% 55%, var(--back-glow) 0%, var(--back-deep) 100%);
  }
  .illustration {
    position: absolute;
    left: 22px;
    top: 64px;
    width: 510px;
    height: 392px;
    border-radius: 48% 48% 20% 20% / 60% 60% 14% 14%;
    background: radial-gradient(ellipse 55% 60% at 50% 42%, var(--illustration) 0%, rgba(244,251,255,0.85) 60%, rgba(244,251,255,0.15) 100%);
  }
  .ground-line {
    position: absolute;
    left: 40px;
    top: 400px;
    width: 460px;
    height: 4px;
    border-radius: 2px;
    background: linear-gradient(90deg, rgba(255,255,255,0), rgba(255,255,255,0.8), rgba(255,255,255,0));
  }
  .text {
    position: absolute;
    margin: 0;
    line-height: 1;
    white-space: nowrap;
    font-weight: 400;
  }
  .title { font-size: 76px; }
  .title--one { left: 428px; top: 62px; }
  .title--two { left: 582px; top: 154px; }
  .contact { font-size: 56px; }
  .contact--name { left: 574px; top: 374px; }
  .contact--phone { left: 574px; top: 446px; }
  .tagline { font-size: 72px; }
  .tagline--one { left: 65px; top: 66px; }
  .tagline--two { left: 229px: top: 153px; }
  .tagline--two { left: 229px; top: 153px; }
  .email { font-size: 46px; left: 117px; top: 380px; }
</style>
</head>
<body>
<main class="canvas">
  <section class="card card--front">
    <div class="illustration" role="img" aria-label="White silhouette of a large spreading tree with a child and a dog resting beneath it"></div>
    <div class="ground-line"></div>
    <h1 class="text title title--one">Reiki for Families</h1>
    <p class="text title title--two">&amp; Pets</p>
    <p class="text contact contact--name">Maren Holloway</p>
    <p class="text contact contact--phone">0400 128 764</p>
  </section>
  <section class="card card--back">
    <p class="text tagline tagline--one">Reiki - relaxes, restores balance</p>
    <p class="text tagline tagline--two">&amp; promotes healing</p>
    <p class="text email">reikiforfamiliesandpets@mailbox.com</p>
  </section>
</main>
</body>
</html>
```